CATALOG COVER

CEDARLINE METAL & EDGE

THE FRONT COVER WILL CONSIST OF THE LOGO & THE BUILDERS CHOICE IN STEEL ROOFING & SIDING, THE FACTORY DIRECT SOURCE. (SAME FONT AS ON THE WEB SITE), PHONE NUMBER WEB SITE AND A STEEL BUILDING. THE BACK OF THE FRONT COVER NEEDS TO HAVE STEEL BUILDING PICTURES, SAME WITH THE INSIDE BACK COVER. AND THE LAST COVER PAGE NEEDS TO CONSIST OF THE LOGO, ADDRESS PICTURES OF BUILDING WEB SITE PHONE NUMBER (23 DIFFERENT COLORS, RESIDENTIAL, COMMERCIAL, AGRICULTURE, CONFINEMENTS, FAST, FRIENDLY QUALITY SERVICE) AND MORE.

WE HAVE LOTS OF PICTURES OF BUILDINGS ON THE WEBSITE THAT YOU CAN USE.
NO NAMES OF EMPLOYEES
ALSO I WANT THE LOGO TO BE ON TOP OF THE FRONT COVER.
PLEASE USE THE SAME FONT FOR FACTORY DIRECT SOURCE AS ON THE WEB SITE

WE MANUFACTURE BUILDINGS AND BUILDING COMPONENTS. EVERYTHING YOU NEED TO DESIGN THIS COVER WILL BE ON WWW.CEDARLINEMETALANDEDGE.EXAMPLE
You will design 4 panels which will be our outside and inside catalog cover.
So it will print both sides of a 11'' x 17'' paper and will be folded and stapled as the cover of the catalog.
please keep in mind we do not have FULL BLEED CAPABILITY.
therefore, images and print must not look like scrapbook.
We have been producing our own catalog for over two years but we desire a professional image. unfortunately we do not have full bleed capability and this has made our attempts look like a scrape book... pasting images and pictures that have borders. please note current catalog available on website.
inside front cover will not have table of contents so it will be "timeless" and not effect out many updates. same with all four panels.
WE ARE LOOKING FOR A PROFESSIONAL COVER
THANKS
Please call with question marty 555-014-2287
Updates

We cannot do FULL BLEED.  If you do not understand please find out what this means.

Also, I have just uploaded quite a bit of material, images to get ideas from.  

Reason: We have made some significant head way on the latest designs. We have posted many attachments since we started We have had excellent two-way feedback from two designers. Hoping we make a "Break Through" to take us to the next level !! Please look at the last four submissions to see our direction. Only one designer captured a way to provide a "fade" to our white cover paper.

can all designers see 3301645 ??

Target Market(s)

CONSTRUCTION COMPANIES AND FARMERS.

Industry/Entity Type

Agriculture

Font styles to use
Serif
Sans Serif

Colors
0555a3
ec2027
ffffff

Requirements
Must have
• PICTURES OF STEEL BUILDINGS AND CONSTRUCTION MATERIAL.
Use image Our Truck with Forklift on back cover, see word doc uploaded
Use images of buildings on inside front cover, see word doc uploaded
Nice to have
• USE THE EXISTING LOGO THAT'S ON FILE.
Use Dark Rich Blues and Reds that Match our Logo
Should not have
• NAMES OF EMPLOYEES OR EMAILS
TABLE OF CONTENTS

```html
<!DOCTYPE html>
<html lang="en">
<head>
<meta charset="utf-8">
<title>Cedarline Metal &amp; Edge — Catalog Cover</title>
<link href="https://fonts.googleapis.com/css2?family=Oswald:wght@500;600&family=Open+Sans:wght@400;600;700&display=swap" rel="stylesheet">
<style>
  :root{
    --stage:#e9ebee;
    --paper:#ffffff;
    --ink:#3a3d42;
    --ink-soft:#55595f;
    --brand-blue:#0555a3;
    --sky-blue:#3f8fd2;
    --pale-blue:#a9cdea;
    --brand-red:#ec2027;
    --photo-sky:#8ea6c4;
    --photo-wall:#b7ab98;
    --photo-ground:#a08e76;
  }
  *{box-sizing:border-box;margin:0;padding:0}
  html,body{width:1200px;height:900px;overflow:hidden}
  body{background:var(--stage);font-family:"Open Sans",Arial,sans-serif;color:var(--ink);position:relative}
  .catalog{position:absolute;left:10px;top:252px;display:flex;gap:30px}
  .spread{display:flex;box-shadow:0 6px 18px rgba(0,0,0,.15)}
  .page{position:relative;width:280px;height:396px;overflow:hidden;background:var(--paper)}
  .cover,.back-cover{box-shadow:0 6px 18px rgba(0,0,0,.15)}
  .spread .page.left{box-shadow:inset -10px 0 14px -10px rgba(0,0,0,.25)}
  .spread .page.right{box-shadow:inset 10px 0 14px -10px rgba(0,0,0,.25)}
  .photo{position:absolute;left:12px;right:12px;top:12px;
    -webkit-mask-image:linear-gradient(180deg,#000 72%,transparent 100%);
    mask-image:linear-gradient(180deg,#000 72%,transparent 100%)}
  .photo.building{background:linear-gradient(180deg,var(--photo-sky) 0%,#c9d3df 30%,var(--photo-wall) 48%,#9d9282 62%,var(--photo-ground) 75%,#b7a58c 100%)}
  .swoosh{position:absolute;left:12px;width:256px}
  .brand-tag{position:absolute;top:20px;right:20px;background:var(--paper);border-radius:4px;padding:5px 8px;display:flex;align-items:center;gap:5px}
  .brand-tag .mark{width:10px;height:10px;background:var(--brand-red)}
  .brand-tag .name{font-family:"Oswald",sans-serif;font-weight:600;font-size:10px;color:var(--brand-blue);letter-spacing:.2px}
  .headline{position:absolute;left:16px;right:12px;top:280px;font-family:"Oswald",sans-serif;font-weight:600;font-size:17px;line-height:1.18;color:var(--ink);text-transform:uppercase}
  .headline .accent{color:var(--sky-blue)}
  .tagline{position:absolute;left:16px;top:323px;font-family:"Oswald",sans-serif;font-weight:500;font-size:7.6px;color:var(--ink);text-transform:uppercase;letter-spacing:.3px}
  .builders-choice{position:absolute;left:16px;top:337px;font-family:"Oswald",sans-serif;font-weight:500;font-size:7.6px;color:var(--brand-blue);text-transform:uppercase;letter-spacing:.3px}
  .factory-direct{position:absolute;left:16px;top:349px;font-family:"Oswald",sans-serif;font-weight:600;font-size:10px;color:var(--brand-red);text-transform:uppercase;letter-spacing:.4px}
  .cover-contact{position:absolute;left:16px;right:14px;top:372px;display:flex;justify-content:space-between;align-items:baseline;font-style:normal;font-size:6.6px;font-weight:700}
  .cover-contact .phone{color:var(--ink);font-size:7.6px}
  .cover-contact .web{color:var(--sky-blue)}
  .intro-column{position:absolute;left:18px;top:20px;width:150px;font-size:6.2px;line-height:1.45;color:var(--ink-soft)}
  .intro-column p+p{margin-top:10px}
  .thumb{position:absolute;left:178px;width:84px;height:84px;border-radius:50%;border:3px solid var(--sky-blue);
    background:linear-gradient(180deg,#c8d2dd 0%,#a8a397 55%,#8f8374 100%)}
  .section-title{position:absolute;font-weight:700;font-size:9px;color:var(--sky-blue);text-transform:uppercase;letter-spacing:.3px}
  .body-copy{position:absolute;font-size:7.2px;line-height:1.55;color:var(--ink);text-align:justify}
  .placeholder-box{position:absolute;left:22px;top:328px;width:48px;height:40px;background:var(--paper);box-shadow:0 0 0 1px #e3e6ea}
  .contact{position:absolute;right:16px;top:326px;text-align:right;font-style:normal;font-size:6.2px;line-height:1.6;color:var(--ink)}
  .contact .phone{font-size:8px;font-weight:600}
  .contact .web{color:var(--sky-blue);font-weight:700}
</style>
</head>
<body>
<main class="catalog">

  <section class="page cover">
    <div class="photo building" style="height:236px" role="img" aria-label="Photo of a tan steel building with covered porch under a blue sky"></div>
    <svg class="swoosh" style="top:170px" width="256" height="110" viewBox="0 0 280 110" preserveAspectRatio="none" aria-hidden="true">
      <path d="M0 66 C90 44 190 28 280 14 L280 110 L0 110 Z" fill="var(--paper)"/>
      <path d="M0 62 C90 40 190 24 280 10" stroke="var(--sky-blue)" stroke-width="9" fill="none"/>
      <path d="M0 74 C90 52 190 36 280 20" stroke="var(--pale-blue)" stroke-width="4" fill="none"/>
      <path d="M0 84 C100 62 200 46 280 34" stroke="var(--pale-blue)" stroke-width="1.5" fill="none"/>
    </svg>
    <div class="brand-tag"><span class="mark"></span><span class="name">CEDARLINE METAL &amp; EDGE</span></div>
    <h1 class="headline">We manufacture <span class="accent">buildings</span><br>and <span class="accent">building components</span></h1>
    <p class="tagline">Suit all your needs &amp; exceed your every expectation</p>
    <p class="builders-choice">The builders choice in steel roofing &amp; siding</p>
    <p class="factory-direct">The factory direct source</p>
    <address class="cover-contact">
      <span class="phone">555-014-2287</span>
      <span class="web">WWW.CEDARLINEMETALANDEDGE.EXAMPLE</span>
    </address>
  </section>

  <div class="spread">
    <section class="page left">
      <div class="intro-column">
        <p>Lorem ipsum dolor sit amet, consectetur adipisicing elit, sed do eiusmod tempor incididunt ut labore et dolore magna aliqua. Lorem ipsum dolor sit amet, consectetur adipisicing elit, sed do eiusmod tempor incididunt ut labore et dolore magna aliqua.</p>
        <p>Lorem ipsum dolor sit amet, consectetur adipisicing elit, sed do eiusmod tempor incididunt ut labore et dolore magna aliqua. Lorem ipsum dolor sit amet, consectetur adipisicing elit, sed do eiusmod tempor incididunt ut labore et dolore magna aliqua.</p>
      </div>
      <div class="thumb" style="top:22px" role="img" aria-label="Round photo of a steel building detail"></div>
      <div class="thumb" style="top:120px" role="img" aria-label="Round photo of a finished steel shop"></div>
      <svg class="swoosh" style="top:210px" width="256" height="80" viewBox="0 0 280 80" preserveAspectRatio="none" aria-hidden="true">
        <path d="M0 40 C90 20 190 18 280 30" stroke="var(--sky-blue)" stroke-width="9" fill="none"/>
        <path d="M0 52 C90 32 190 30 280 42" stroke="var(--pale-blue)" stroke-width="4" fill="none"/>
        <path d="M0 62 C100 44 200 42 280 54" stroke="var(--pale-blue)" stroke-width="1.5" fill="none"/>
      </svg>
      <h2 class="section-title" style="left:18px;top:292px">Our Assurance</h2>
      <p class="body-copy" style="left:18px;right:18px;top:308px">Lorem ipsum dolor sit amet, consectetur adipisicing elit, sed do eiusmod tempor incididunt ut labore et dolore magna aliqua. Ut enim ad minim veniam. Lorem ipsum dolor sit amet, consectetur adipisicing elit, sed do eiusmod tempor incididunt ut labore et dolore magna aliqua. Ut enim ad minim veniam. Lorem ipsum dolor sit amet, consectetur adipisicing elit, sed do eiusmod tempor incididunt ut labore.</p>
    </section>
    <section class="page right">
      <div class="photo building" style="height:268px" role="img" aria-label="Photo of a steel-roofed home and shop under an overcast sky"></div>
      <svg class="swoosh" style="top:196px" width="256" height="100" viewBox="0 0 280 100" preserveAspectRatio="none" aria-hidden="true">
        <path d="M0 48 C90 34 190 36 280 50 L280 100 L0 100 Z" fill="var(--paper)"/>
        <path d="M0 44 C90 30 190 32 280 46" stroke="var(--sky-blue)" stroke-width="9" fill="none"/>
        <path d="M0 56 C90 42 190 44 280 58" stroke="var(--pale-blue)" stroke-width="4" fill="none"/>
      </svg>
    </section>
  </div>

  <section class="page back-cover">
    <div class="photo building" style="height:224px" role="img" aria-label="Photo of a grey steel shop with overhead doors and a covered entry"></div>
    <svg class="swoosh" style="top:120px" width="256" height="130" viewBox="0 0 280 130" preserveAspectRatio="none" aria-hidden="true">
      <path d="M0 32 C80 52 180 92 280 110 L280 130 L0 130 Z" fill="var(--paper)"/>
      <path d="M0 28 C80 48 180 88 280 106" stroke="var(--sky-blue)" stroke-width="6" fill="none"/>
      <path d="M0 40 C80 60 180 100 280 118" stroke="var(--pale-blue)" stroke-width="4" fill="none"/>
      <path d="M0 18 C80 38 180 78 280 96" stroke="var(--pale-blue)" stroke-width="1.5" fill="none"/>
    </svg>
    <h2 class="section-title" style="left:22px;top:252px">Enoy Yachting</h2>
    <p class="body-copy" style="left:22px;right:18px;top:268px">Lorem ipsum dolor sit amet, consectetur adipisicing elit, sed do eiusmod tempor incididunt ut labore et dolore magna aliqua. Ut enim ad minim veniam. Lorem ipsum dolor sit amet, consectetur adipisicing elit, sed do eiusmod tempor.</p>
    <div class="placeholder-box" aria-hidden="true"></div>
    <address class="contact">
      <div class="phone">555 014 3390</div>
      <div>social.example/cedarlinemetal</div>
      <div>updates.example/cedarlinemetal</div>
      <div class="web">WWW.CEDARLINEMETALANDEDGE.EXAMPLE</div>
    </address>
  </section>

</main>
</body>
</html>
```